"BREAKING NEWS!" Fitness photos needed

Hello.... We are creating our new ads for Pellumra and Quorvidel and we need some photos manipulated and text added.

We have 5 photos total that we would like to have the Headline read "Breaking News" and we'll be split testing two different quotes, so I'd like to have:

AD #1:
Breaking News - Finally! Ridgecrest Gets the Gym That Actually Delivers Results (and It's Fun!)

And then a second set on the same photos that read:

AD #2:
Breaking News - Ridgecrest Residents Ditch Boring Workouts for This Life-Changing Fitness Experience

I'd like the photos to pop and stand out, so if color corrections need to be done, please feel free.

I've attached all photos and an example photo that DOES NOT need to be the same. It's just an example I saw that caught my eye, but I feel could be done better.

Thank you!

```html
<!DOCTYPE html>
<html lang="en">
<head>
<meta charset="utf-8">
<title>Breaking News – Fitness Ads</title>
<link rel="stylesheet" href="https://fonts.googleapis.com/css2?family=Big+Shoulders+Stencil+Display:wght@800&family=Comfortaa:wght@300&family=Oswald:wght@700&family=Roboto+Condensed:wght@500&display=swap">
<style>
  :root {
    --board: #f1f1f1;
    --plum: #24103a;
    --white: #ffffff;
    --ink: #0d0b08;
    --gold: #e9cf0f;
    --violet: #5a48a6;
    --wall-yellow: #f2d81a;
    --legging-plum: #5a2344;
    --floor-grey: #3b3d45;
    --shirt-navy: #1f2640;
    --ceiling: #e4e0da;
  }
  * { margin: 0; padding: 0; box-sizing: border-box; }
  html, body { width: 808px; height: 1200px; overflow: hidden; background: var(--board); }
  .board { position: relative; width: 808px; height: 1200px; }

  .ad { position: absolute; left: 132px; width: 544px; height: 544px; overflow: hidden; }
  .ad--finally { top: 46px; background: var(--plum); box-shadow: 0 4px 10px rgba(0,0,0,0.25); }
  .ad--ditch {
    top: 620px;
    background: linear-gradient(35deg, var(--gold) 0%, #bfa432 40%, #957c5a 72%, var(--violet) 100%);
  }

  .ad__art { position: absolute; inset: 0; width: 100%; height: 100%; }

  .stencil-head {
    position: absolute; left: 28px; color: var(--white);
    font-family: "Big Shoulders Stencil Display", sans-serif; font-weight: 800;
    line-height: 1; white-space: nowrap;
  }
  .stencil-head--top { top: 291px; font-size: 88px; letter-spacing: 1px; }
  .stencil-head--bottom { top: 372px; font-size: 53px; letter-spacing: 1px; }
  .ad__tagline {
    position: absolute; left: 28px; top: 447px; color: var(--white);
    font-family: "Comfortaa", sans-serif; font-weight: 300; font-size: 12.5px; line-height: 18px;
  }

  .photo { position: absolute; box-shadow: 3px 6px 10px rgba(0,0,0,0.45); }
  .photo--rows { left: 27px; top: 19px; width: 236px; height: 271px;
    background:
      radial-gradient(ellipse 30% 45% at 52% 78%, var(--legging-plum) 0%, rgba(90,35,68,0) 100%),
      radial-gradient(ellipse 28% 22% at 48% 32%, #1b1b22 0%, rgba(27,27,34,0) 100%),
      radial-gradient(ellipse 40% 22% at 85% 50%, var(--wall-yellow) 0%, rgba(242,216,26,0) 100%),
      linear-gradient(180deg, var(--ceiling) 0%, #c9bcae 38%, #6e6a70 70%, var(--floor-grey) 100%); }
  .photo--press { left: 263px; top: 19px; width: 253px; height: 189px;
    background:
      radial-gradient(ellipse 18% 45% at 76% 62%, var(--shirt-navy) 0%, rgba(31,38,64,0) 100%),
      radial-gradient(ellipse 20% 40% at 4% 30%, var(--wall-yellow) 0%, rgba(242,216,26,0) 100%),
      radial-gradient(ellipse 14% 35% at 96% 25%, var(--wall-yellow) 0%, rgba(242,216,26,0) 100%),
      linear-gradient(180deg, #c9c6c0 0%, #a5a29c 45%, #4b4d55 75%, var(--floor-grey) 100%); }
  .photo--overhead { left: 294px; top: 223px; width: 194px; height: 143px;
    background:
      radial-gradient(ellipse 20% 30% at 62% 82%, #3e4a34 0%, rgba(62,74,52,0) 100%),
      radial-gradient(ellipse 22% 40% at 8% 30%, var(--wall-yellow) 0%, rgba(242,216,26,0) 100%),
      linear-gradient(180deg, #cfccc6 0%, #a8a49c 45%, #55565a 78%, var(--floor-grey) 100%); }

  .glass { position: absolute; background: rgba(255,255,255,0.55); }
  .glass--solid { background: var(--white); }

  .ditch__headline {
    position: absolute; left: 0; right: 0; top: 424px; text-align: center; color: var(--ink);
    font-family: "Oswald", sans-serif; font-weight: 700; font-size: 50px; line-height: 1;
    transform: scaleX(1.36); transform-origin: center;
  }
  .ditch__tagline {
    position: absolute; left: 0; right: 0; top: 494px; text-align: center; color: var(--ink);
    font-family: "Roboto Condensed", sans-serif; font-weight: 500; font-size: 12px;
  }
</style>
</head>
<body>
<main class="board">

  <section class="ad ad--finally">
    <svg class="ad__art" viewBox="0 0 646 646" preserveAspectRatio="none">
      <defs>
        <clipPath id="rowArea"><polygon points="0,0 646,0 646,7 163,315 0,190"/></clipPath>
        <clipPath id="pressArea"><polygon points="291,280 646,55 646,485"/></clipPath>
        <linearGradient id="rowBase" x1="0" y1="0" x2="0" y2="1">
          <stop offset="0" stop-color="#e4e0da"/>
          <stop offset="0.4" stop-color="#c7b9a9"/>
          <stop offset="1" stop-color="#5b4b58"/>
        </linearGradient>
        <radialGradient id="rowYellow" cx="0.5" cy="0.5" r="0.5">
          <stop offset="0" stop-color="#f2d81a"/><stop offset="1" stop-color="#f2d81a" stop-opacity="0"/>
        </radialGradient>
        <radialGradient id="rowDark" cx="0.5" cy="0.5" r="0.5">
          <stop offset="0" stop-color="#1b1b22"/><stop offset="1" stop-color="#1b1b22" stop-opacity="0"/>
        </radialGradient>
        <radialGradient id="rowPlum" cx="0.5" cy="0.5" r="0.5">
          <stop offset="0" stop-color="#5a2344"/><stop offset="1" stop-color="#5a2344" stop-opacity="0"/>
        </radialGradient>
        <linearGradient id="pressBase" x1="0" y1="0" x2="0" y2="1">
          <stop offset="0" stop-color="#cfcbc4"/>
          <stop offset="0.5" stop-color="#8e8c8a"/>
          <stop offset="1" stop-color="#3b3d45"/>
        </linearGradient>
        <radialGradient id="pressNavy" cx="0.5" cy="0.5" r="0.5">
          <stop offset="0" stop-color="#1f2640"/><stop offset="1" stop-color="#1f2640" stop-opacity="0"/>
        </radialGradient>
      </defs>
      <g clip-path="url(#rowArea)" role="img" aria-label="Photo of a woman doing a dumbbell row in the gym">
        <rect width="646" height="320" fill="url(#rowBase)"/>
        <ellipse cx="440" cy="170" rx="170" ry="70" fill="url(#rowYellow)"/>
        <ellipse cx="40" cy="250" rx="90" ry="60" fill="url(#rowYellow)"/>
        <ellipse cx="270" cy="200" rx="120" ry="110" fill="url(#rowDark)"/>
        <ellipse cx="250" cy="290" rx="120" ry="60" fill="url(#rowPlum)"/>
      </g>
      <polyline points="0,190 163,315 646,7" fill="none" stroke="var(--white)" stroke-width="6"/>
      <g clip-path="url(#pressArea)" role="img" aria-label="Photo of a woman pressing a dumbbell overhead on a bench">
        <rect x="290" y="50" width="356" height="440" fill="url(#pressBase)"/>
        <ellipse cx="600" cy="360" rx="110" ry="180" fill="url(#pressNavy)"/>
        <ellipse cx="480" cy="310" rx="90" ry="60" fill="url(#rowDark)"/>
      </g>
      <line x1="291" y1="280" x2="646" y2="55" stroke="var(--white)" stroke-width="4"/>
      <polyline points="284,288 640,515 646,515" fill="none" stroke="var(--white)" stroke-width="2"/>
      <polygon fill="var(--white)" points="283,646 552,481 646,535 646,646"/>
    </svg>
    <div class="stencil-head stencil-head--top">BREAKING</div>
    <div class="stencil-head stencil-head--bottom">NEWS - FINALLY</div>
    <p class="ad__tagline">Ridgecrest Gets the Gym That<br>Actually Delivers Results (and It's Fun!)</p>
  </section>

  <section class="ad ad--ditch">
    <div class="photo photo--rows" role="img" aria-label="Photo of a woman doing a dumbbell row beside a bench"></div>
    <div class="photo photo--press" role="img" aria-label="Photo of a class pressing dumbbells overhead on benches"></div>
    <div class="photo photo--overhead" role="img" aria-label="Photo of women seated on benches lifting dumbbells overhead"></div>
    <div class="glass glass--solid" style="left:0;top:104px;width:36px;height:63px;opacity:.85"></div>
    <div class="glass glass--solid" style="left:101px;top:255px;width:24px;height:86px"></div>
    <div class="glass" style="left:231px;top:19px;width:34px;height:59px"></div>
    <div class="glass" style="left:280px;top:104px;width:61px;height:152px"></div>
    <h1 class="ditch__headline">BREAKING NEWS</h1>
    <p class="ditch__tagline">Ridgecrest Residents Ditch Boring Workouts for This Life-Changing Fitness Experience</p>
  </section>

</main>
</body>
</html>
```